Standard logo business card

We are seeking a solid, somewhat understated professional design. We are a tech company. We like fonts similar to Aptifer Slab. Front side will be white with the contact information and a small version of our primary (Light background) logo.

(We have three people so we will have three names and titles)

Back side will hold our reverse logo on dark background along with the tagline:

"Intelligent annotation solutions for complex data"

Target Market(s)

Professionals, Tech

Industry/Entity Type

Business

Contact Information for Business Card

Name
Title

Phone
Email
City, State
Website

[We will email leading designer specific contact information)

Font styles to use
Serif

Requirements
Must have
• Colors are:
• Orange RGB 245,92,23
• Blue RGB 3,34,56
Nice to have
• We like a split with the Name and Title on the right and then contact details (below) on the left.

```html
<!DOCTYPE html>
<html lang="en">
<head>
<meta charset="utf-8">
<title>Corvanta Business Card</title>
<link href="https://fonts.googleapis.com/css2?family=Crimson+Text:ital,wght@0,400;0,700;1,400&display=swap" rel="stylesheet">
<style>
  :root {
    --orange: rgb(245, 92, 23);
    --blue: rgb(3, 34, 56);
    --black: #050505;
    --white: #ffffff;
    --paper: #f6f6f4;
    --backdrop: #e4e2de;
  }
  * { margin: 0; padding: 0; box-sizing: border-box; }
  html, body {
    width: 1200px;
    height: 1037px;
    overflow: hidden;
    background: var(--backdrop);
    font-family: "Crimson Text", Georgia, serif;
  }
  .card {
    position: absolute;
    width: 640px;
    height: 366px;
    overflow: hidden;
    box-shadow: 0 6px 18px rgba(0, 0, 0, 0.18);
  }
  .wordmark {
    display: flex;
    align-items: center;
    gap: 10px;
    font-weight: 700;
    line-height: 1;
  }
  .wordmark .mark {
    background: var(--orange);
    flex: none;
  }

  /* Dark side: reverse logo and tagline */
  .card-back {
    left: 370px;
    top: 70px;
    background: var(--blue);
    color: var(--white);
  }
  .tagline {
    position: absolute;
    left: 44px;
    top: 150px;
    font-size: 21px;
    font-weight: 700;
    color: var(--orange);
  }
  .accent-band {
    position: absolute;
    left: 0;
    right: 0;
    bottom: 0;
    height: 128px;
    background: var(--orange);
  }
  .logo-tab {
    position: absolute;
    left: 240px;
    right: 0;
    top: 22px;
    height: 86px;
    background: var(--black);
    border-radius: 43px 0 0 43px;
  }
  .logo-tab .wordmark {
    position: absolute;
    right: 34px;
    top: 14px;
    font-size: 56px;
    color: var(--white);
  }
  .logo-tab .mark { width: 30px; height: 30px; }

  /* Light side: small logo and contact details */
  .card-front {
    left: 150px;
    top: 560px;
    background: var(--paper);
    color: var(--blue);
  }
  .card-front .wordmark {
    position: absolute;
    left: 40px;
    top: 34px;
    font-size: 36px;
  }
  .card-front .mark { width: 20px; height: 20px; }
  .identity {
    position: absolute;
    right: 44px;
    top: 128px;
    text-align: right;
  }
  .identity .name {
    font-size: 24px;
    font-variant: small-caps;
    letter-spacing: 1px;
    line-height: 1.1;
  }
  .identity .title {
    font-size: 16px;
    font-style: italic;
    color: var(--orange);
  }
  .contact-list {
    position: absolute;
    left: 40px;
    top: 120px;
    list-style: none;
    font-size: 15px;
    font-style: italic;
    line-height: 20px;
  }
  .contact-list li {
    display: flex;
    align-items: flex-start;
    gap: 10px;
  }
  .contact-list .icon {
    width: 13px;
    height: 13px;
    margin-top: 4px;
    flex: none;
    color: var(--orange);
  }
  .contact-list .indent { padding-left: 23px; }
  .base-band {
    position: absolute;
    left: 0;
    right: 0;
    bottom: 0;
    height: 64px;
    background: var(--blue);
  }
</style>
</head>
<body>

<section class="card card-back">
  <p class="tagline">Intelligent annotation solutions for complex data</p>
  <div class="accent-band">
    <div class="logo-tab">
      <div class="wordmark"><span class="mark"></span><span>corvanta</span></div>
    </div>
  </div>
</section>

<section class="card card-front">
  <div class="wordmark"><span class="mark"></span><span>corvanta</span></div>

  <ul class="contact-list">
    <li>
      <svg class="icon" viewBox="0 0 12 12"><path d="M6 0.5a3.8 3.8 0 0 0-3.8 3.8C2.2 7 6 11.5 6 11.5S9.8 7 9.8 4.3A3.8 3.8 0 0 0 6 0.5z" fill="currentColor"/><circle cx="6" cy="4.3" r="1.4" fill="var(--paper)"/></svg>
      <span>Your City</span>
    </li>
    <li class="indent">Your State</li>
    <li>
      <svg class="icon" viewBox="0 0 12 12"><rect x="0.6" y="2.4" width="10.8" height="7.2" fill="none" stroke="currentColor"/><path d="M0.6 2.4 6 6.6l5.4-4.2" fill="none" stroke="currentColor"/></svg>
      <span>Your Email.com</span>
    </li>
    <li>
      <svg class="icon" viewBox="0 0 12 12"><rect x="3" y="0.6" width="6" height="10.8" rx="1" fill="none" stroke="currentColor"/><line x1="5" y1="9.4" x2="7" y2="9.4" stroke="currentColor"/></svg>
      <span>Your Phone Number</span>
    </li>
    <li>
      <svg class="icon" viewBox="0 0 12 12"><circle cx="6" cy="6" r="5.2" fill="none" stroke="currentColor"/><ellipse cx="6" cy="6" rx="2.3" ry="5.2" fill="none" stroke="currentColor"/><line x1="0.8" y1="6" x2="11.2" y2="6" stroke="currentColor"/></svg>
      <span>Your Website</span>
    </li>
  </ul>

  <div class="identity">
    <div class="name">Your Name</div>
    <div class="title">Title</div>
  </div>

  <div class="base-band"></div>
</section>

</body>
</html>
```